Redesign Quorvix.com Front Landing Page To Give It The Wow Factor Keeping SEO and Page Load Speeds

We need to redesign the landing page of www.quorvix.com to give it the wow factor

It must have exactly the same content, page size (currently 5.04 KB) or (5,156 bytes) and speed of the current site and rank 100/100 with Tallbeck.com tools as the page currently does.

This of course is subjective to content - in other words for an outstanding design - leeway will be given - THE WOW FACTOR IS CRITICAL.

THE PAGE MUST BE HTML5 COMPLIANT AND TOTALLY COMPLETE INCLUDING ANY SCRIPTS, CSS ETC, AND READY TO UPLOAD THE HTML PAGE AND CONTENT FOLDER TO THE SERVER WITH NO MODIFICATIONS REQUIRED.

SERVER IS CURRENTLY WINDOWS 2008 DATACENTER R2 BUT WILL SHORTLY BE UPGRADED TO WINDOWS 2012 DATACENTER R2 SERVER.

The current landing page loads faster that 96 % of the sites on the web according to Tallbeck Tools and that is on our current cable line connection that we are using while site is in development.

So we are looking for a fully optimized page that gives a outstanding first impression and SEO optimized.

It must be fully responsive for all screen size and utilize full page design on larger screen sizes.

The logo will remain to be strictly CSS and there are to be no images used on landing page other than the category link pages, all images must be fully optimized yet sharp and crisp.

A CSS content slider may be used to replace the Javascript rotator currently used - example www.vendrofade.com - we do have a licence for that slider

The winner will also be asked to look at the main script page and given priority in a contest for that as well.

Target Market(s)

World Online Trading Advertising and Business Directory Community Members

Industry/Entity Type

Seo

Requirements
Must have
• A feel of community - must be simple and clean.
• HTML5 Compliant
• Fully SEO optimized but not keyword spammed
• Keep the same content and links as existing landing page
• Search must be fully working and same as current options
Nice to have
• A WOW factor CSS slider - not bloated
Should not have
• No flash or any content that would slow down the front landing page Load Times

```html
<!DOCTYPE html>
<html lang="en">
<head>
<meta charset="utf-8">
<title>Quorvix – Free Ads, Auctions, Buy, Sell, Trade, Wanted</title>
<link href="https://fonts.googleapis.com/css2?family=Roboto:ital,wght@0,400;0,500;0,700;0,900;1,900&display=swap" rel="stylesheet">
<style>
:root{
  --orange:#d9540b;
  --orange-dark:#c24a08;
  --sky:#5bb5ec;
  --sky-deep:#3f9fdd;
  --nav:#1d7fc3;
  --nav-line:#1670ad;
  --maroon:#a3155b;
  --ink:#333;
  --muted:#555;
  --rule:#e3e3e3;
  --panel:#f1f1f1;
  --panel-line:#d9d9d9;
  --white:#fff;
}
*{box-sizing:border-box;margin:0;padding:0}
html,body{width:911px;height:1200px;overflow:hidden}
body{font-family:"Roboto",Arial,sans-serif;color:var(--ink);background:var(--white);position:relative}
a{color:inherit;text-decoration:none}
.wrap{position:absolute;left:84px;width:744px}

/* top strip */
.topbar{position:absolute;top:0;left:0;width:911px;height:26px;background:var(--orange);color:var(--white);font-size:9.5px;text-transform:uppercase}
.topbar .region{position:absolute;left:84px;top:8px}
.topbar .region b{font-weight:400;margin-left:4px}
.topbar .region svg{margin-left:4px;vertical-align:middle}
.toplinks{position:absolute;right:84px;top:0;display:flex;height:26px;align-items:center}
.toplinks a{padding:0 10px;border-left:1px solid rgba(255,255,255,.45)}
.toplinks a:first-child{border-left:0}
.toplinks a:last-child{padding-right:0}

/* header */
.header{position:absolute;top:26px;left:0;width:911px;height:88px;background:var(--sky)}
.logo{position:absolute;left:84px;top:31px;font-size:21px;font-weight:700;color:var(--white)}
.search{position:absolute;left:190px;top:31px;width:273px;height:27px;border-radius:14px;background:var(--nav);display:flex;align-items:center;font-size:10px;color:var(--white)}
.search .field{flex:1;padding-left:12px}
.search .cat{width:90px;height:100%;border-left:1px solid var(--nav-line);display:flex;align-items:center;padding-left:10px;gap:18px}
.search .go{width:28px;display:flex;justify-content:center}
.tagline{position:absolute;right:84px;top:24px;text-align:right;color:var(--white)}
.tagline h2{font-size:15px;font-weight:500;letter-spacing:.2px}
.tagline p{margin-top:8px;padding-top:6px;border-top:1px solid rgba(255,255,255,.5);font-size:9.5px;text-align:center}

/* nav */
.nav{position:absolute;top:114px;left:0;width:911px;height:32px;background:var(--nav);font-size:9.5px;color:var(--white);text-transform:uppercase}
.nav .main{position:absolute;left:84px;top:0;display:flex;height:32px}
.nav .main a{display:flex;align-items:center;padding:0 15px}
.nav .main a.on{background:var(--orange);padding:0 16px}
.nav .side{position:absolute;right:84px;top:0;display:flex;height:32px;align-items:center;gap:18px}

/* hero */
.hero{position:absolute;top:146px;left:0;width:911px;height:260px;background:linear-gradient(135deg,#eef6fc 0%,#dcebf7 50%,#eaf4fb 100%)}
.hero .kicker{position:absolute;left:188px;top:72px;font-size:11px;color:#888}
.hero h1{position:absolute;left:180px;top:86px;font-size:22px;font-weight:900;font-style:italic;color:var(--orange);letter-spacing:-.2px}
.hero .sub{position:absolute;left:326px;top:112px;font-size:14px;font-weight:500;color:#222}
.hero .cta{position:absolute;left:383px;top:136px;font-size:10px;color:#333;display:flex;align-items:center;gap:6px}
.hero .art{position:absolute;left:556px;top:42px;width:212px;height:170px;border-radius:40% 45% 30% 35%;background:radial-gradient(circle at 40% 40%,#f3f1ea 0%,#c9c2ad 45%,#8d7d54 80%,rgba(141,125,84,0) 100%)}
.dots{position:absolute;left:426px;top:234px;display:flex;gap:7px}
.dots i{width:6px;height:6px;border-radius:50%;background:#b9d8ee}
.dots i.on{background:var(--sky-deep)}

/* categories */
.cats{position:absolute;left:84px;top:378px;width:171px;height:714px;background:var(--panel);border:1px solid var(--panel-line);border-top:0;border-radius:0 0 4px 4px}
.cats h3{height:28px;background:var(--sky);color:var(--white);font-size:10.5px;font-weight:500;display:flex;align-items:center;padding-left:12px;gap:8px;text-transform:uppercase;margin:0 -1px}
.cats ul{list-style:none;padding:10px 0 0 12px}
.cats li{height:20.9px;font-size:9.5px;color:var(--muted);display:flex;align-items:center;gap:6px}
.cats li::before{content:"";width:4px;height:4px;border:1px solid var(--orange);border-radius:50%}
.cats li.on{color:var(--orange)}
.cats li.on::before{background:var(--orange)}

/* listings */
.block{position:absolute;left:275px;width:551px}
.block h3{font-size:13px;font-weight:500;color:var(--orange);height:24px;border-bottom:1px solid var(--rule);position:relative}
.arrows{position:absolute;right:0;top:0;display:flex;gap:3px}
.arrows span{width:16px;height:16px;display:flex;align-items:center;justify-content:center;background:var(--white)}
.arrows span.on{background:var(--orange)}
.items{display:flex;gap:10px;margin-top:7px}
.item{width:102px;text-align:center}
.item .pic{height:113px}
.item .name{font-size:10px;color:var(--muted);margin-top:11px}
.item .price{font-size:10px;color:var(--orange);margin-top:5px}
.p-pig{background:linear-gradient(160deg,#5f8a48 0%,#e9b59a 40%,#d99780 75%,#7a8f5a 100%)}
.p-server{background:linear-gradient(180deg,#fff 25%,#9ea3a6 45%,#6d7276 55%,#fff 75%)}
.p-horse{background:linear-gradient(160deg,#5a7f3d 0%,#e0592a 40%,#c94a1e 70%,#8a6b4a 100%)}
.p-fab{background:linear-gradient(160deg,#6e8a4f 0%,#2a2a2a 40%,#e7c21c 75%,#5a6b3e 100%)}
.p-hair{background:linear-gradient(160deg,#111 0%,#222 55%,#6b5320 100%)}

.advantage{position:absolute;left:275px;top:640px;width:564px;height:64px;display:flex}
.advantage .tag{width:98px;background:var(--maroon);color:var(--white);font-size:12px;font-weight:700;display:flex;align-items:center;justify-content:center;text-align:center;line-height:1.2;text-transform:uppercase}
.advantage .msg{flex:1;background:var(--sky);color:var(--white);text-align:center;font-size:10px;display:flex;flex-direction:column;justify-content:center;gap:6px}
.advantage .msg b{font-weight:500}
.advantage .edge{width:7px;background:var(--maroon)}

/* footer */
.footer{position:absolute;top:1162px;left:0;width:911px;height:38px;background:var(--orange);color:var(--white);font-size:9px}
.footer p{position:absolute;left:84px;top:14px}
.social{position:absolute;right:84px;top:9px;display:flex;gap:10px}
.social i{width:19px;height:19px;border:1px solid rgba(255,255,255,.6);border-radius:50%}
</style>
</head>
<body>

<div class="topbar">
  <div class="region">Select your region : <b>United States</b><svg width="7" height="5" viewBox="0 0 7 5"><path d="M0 0h7L3.5 5z" fill="#fff"/></svg></div>
  <nav class="toplinks"><a href="#">Features</a><a href="#">Map Listing</a><a href="#">Post Free Add</a><a href="#">Post Free Auction</a></nav>
</div>

<header class="header">
  <a class="logo" href="#">Quorvix</a>
  <form class="search">
    <span class="field">Search...</span>
    <span class="cat">All Categories<svg width="7" height="5" viewBox="0 0 7 5"><path d="M0 0h7L3.5 5z" fill="#fff"/></svg></span>
    <span class="go"><svg width="10" height="10" viewBox="0 0 10 10"><circle cx="4" cy="4" r="3" fill="none" stroke="#fff" stroke-width="1.6"/><path d="M6.2 6.2L9 9" stroke="#fff" stroke-width="1.8"/></svg></span>
  </form>
  <div class="tagline">
    <h2>Free Ads - Auctions - Buy - Sell - Trade - Wanted</h2>
    <p>* Global * Regional * Local * Auction Classified &amp; Directory Listings</p>
  </div>
</header>

<nav class="nav">
  <div class="main"><a class="on" href="#">Home</a><a href="#">About Us</a><a href="#">Community</a><a href="#">Site Map</a><a href="#">Help</a><a href="#">Contact Us</a></div>
  <div class="side"><a href="#">+ Search</a><a href="#">Stores</a></div>
</nav>

<section class="hero">
  <p class="kicker">Feel the real</p>
  <h1>ANTIQUES &amp; COLLECTABLES</h1>
  <p class="sub">classifieds &amp; auctions</p>
  <a class="cta" href="#">CHECKOUT ALL <svg width="9" height="9" viewBox="0 0 9 9"><circle cx="4.5" cy="4.5" r="4.5" fill="#d9540b"/><path d="M3.5 2.5l2 2-2 2" stroke="#fff" stroke-width="1.2" fill="none"/></svg></a>
  <div class="art" role="img" aria-label="Silver trophy cup, compass and gold jewellery rings"></div>
  <div class="dots"><i class="on"></i><i></i><i></i><i></i><i></i></div>
</section>

<aside class="cats">
  <h3><svg width="10" height="8" viewBox="0 0 10 8"><path d="M0 1h10M0 4h10M0 7h10" stroke="#fff" stroke-width="1.5"/></svg>Browse All Categories</h3>
  <ul>
    <li class="on">Activities &amp; Events</li><li>Antiques &amp; Collectables</li><li>Automotive &amp; Vehicles</li><li>Aviation &amp; Planes</li><li>Boats &amp; Watercraft</li><li>Business Directory</li><li>Business to Business</li><li>Charities &amp; Non Profits</li><li>Clothing &amp; Accessories</li><li>Computing &amp; Networking</li><li>Construction &amp; Logging</li><li>Daily Deals &amp; Services</li><li>Dining-Food &amp; Beverages</li><li>Education &amp; Training</li><li>Electronics &amp; Phones</li><li>Employment &amp; Careers</li><li>Farming &amp; Agriculture</li><li>Heavy Trucks &amp; Trailers</li><li>Home &amp; Garden</li><li>Industrial Machinery</li><li>Jewelry &amp; Watches</li><li>Motorsports &amp; Racing</li><li>Office &amp; Restaurant</li><li>Personal Services</li><li>Photography &amp;Equipment</li><li>Public News &amp; Events</li><li>Real Estate &amp; Rentals</li><li>Resorts Tickets &amp; Travel</li><li>Sporting Goods &amp; Act.</li><li>RV'S Trailers &amp; Access..</li><li>Tools Hand/Power</li><li>Wanted &amp; Barter/Free</li>
  </ul>
</aside>

<section class="block" style="top:430px">
  <h3>Featured Listings<span class="arrows"><span class="on"><svg width="6" height="8" viewBox="0 0 6 8"><path d="M5 0L1 4l4 4" stroke="#fff" stroke-width="1.6" fill="none"/></svg></span><span><svg width="6" height="8" viewBox="0 0 6 8"><path d="M1 0l4 4-4 4" stroke="#d9540b" stroke-width="1.6" fill="none"/></svg></span></span></h3>
  <div class="items">
    <div class="item"><div class="pic p-pig" role="img" aria-label="Pig shaped mailbox on a post"></div><p class="name">Pig Mailbox</p><p class="price">$ 129.00</p></div>
    <div class="item"><div class="pic p-server" role="img" aria-label="Rack mounted server unit"></div><p class="name">Micro Cloud Server</p><p class="price">$ 9,637.63</p></div>
    <div class="item"><div class="pic p-horse" role="img" aria-label="Horse shaped mailbox on a post"></div><p class="name">Horse Mailbox</p><p class="price">$ 129.00</p></div>
    <div class="item"><div class="pic p-fab" role="img" aria-label="Yellow and black loader attachment"></div><p class="name">RT Fabrications</p><p class="price">$ 15,750.00</p></div>
    <div class="item"><div class="pic p-hair" role="img" aria-label="Hair studio sign on black"></div><p class="name">Marlow Vane Haircut</p><p class="price">$ 129.00</p></div>
  </div>
</section>

<aside class="advantage">
  <div class="tag">The Quorvix<br>Advantage</div>
  <div class="msg"><span>CHECK OUT WHAT WE OFFERS VS THE OTHER GUYS?</span><b>Get the best service and features for free!!</b></div>
  <div class="edge"></div>
</aside>

<section class="block" style="top:723px">
  <h3>Hottest Listings<span class="arrows"><span><svg width="6" height="8" viewBox="0 0 6 8"><path d="M5 0L1 4l4 4" stroke="#d9540b" stroke-width="1.6" fill="none"/></svg></span><span><svg width="6" height="8" viewBox="0 0 6 8"><path d="M1 0l4 4-4 4" stroke="#d9540b" stroke-width="1.6" fill="none"/></svg></span></span></h3>
  <div class="items">
    <div class="item"><div class="pic p-pig" role="img" aria-label="Pig shaped mailbox on a post"></div><p class="name">Pig Mailbox</p><p class="price">$ 129.00</p></div>
    <div class="item"><div class="pic p-server" role="img" aria-label="Rack mounted server unit"></div><p class="name">Micro Cloud Server</p><p class="price">$ 9,637.63</p></div>
    <div class="item"><div class="pic p-horse" role="img" aria-label="Horse shaped mailbox on a post"></div><p class="name">Horse Mailbox</p><p class="price">$ 129.00</p></div>
    <div class="item"><div class="pic p-fab" role="img" aria-label="Yellow and black loader attachment"></div><p class="name">RT Fabrications</p><p class="price">$ 15,750.00</p></div>
    <div class="item"><div class="pic p-hair" role="img" aria-label="Hair studio sign on black"></div><p class="name">Marlow Vane Haircut</p><p class="price">$ 129.00</p></div>
  </div>
</section>

<section class="block" style="top:932px">
  <h3>Recent Listings<span class="arrows"><span><svg width="6" height="8" viewBox="0 0 6 8"><path d="M5 0L1 4l4 4" stroke="#d9540b" stroke-width="1.6" fill="none"/></svg></span><span><svg width="6" height="8" viewBox="0 0 6 8"><path d="M1 0l4 4-4 4" stroke="#d9540b" stroke-width="1.6" fill="none"/></svg></span></span></h3>
  <div class="items">
    <div class="item"><div class="pic p-pig" role="img" aria-label="Pig shaped mailbox on a post"></div><p class="name">Pig Mailbox</p><p class="price">$ 129.00</p></div>
    <div class="item"><div class="pic p-server" role="img" aria-label="Rack mounted server unit"></div><p class="name">Micro Cloud Server</p><p class="price">$ 9,637.63</p></div>
    <div class="item"><div class="pic p-horse" role="img" aria-label="Horse shaped mailbox on a post"></div><p class="name">Horse Mailbox</p><p class="price">$ 129.00</p></div>
    <div class="item"><div class="pic p-fab" role="img" aria-label="Yellow and black loader attachment"></div><p class="name">RT Fabrications</p><p class="price">$ 15,750.00</p></div>
    <div class="item"><div class="pic p-hair" role="img" aria-label="Hair studio sign on black"></div><p class="name">Marlow Vane Haircut</p><p class="price">$ 129.00</p></div>
  </div>
</section>

<footer class="footer">
  <p>© Copyright Quorvix.com 2015 - 2016. All rights reserved. Your Free No Credit Cards Required Classifieds Site</p>
  <div class="social"><i></i><i></i><i></i></div>
</footer>

</body>
</html>
```